QUORVIX - Sydney Based Technology Consultancy -Logo & Business Card design

Who are we?
-
Quorvix is an emerging and advanced technology consulting and professional services business based in Sydney, Australia. Quorvix specialising in increasing value to organisations through the effective use of current and emerging technologies, ensuring that technology is a sustainable catalyst to attaining stated business goals.

We pride ourselves in challenging the norm.

What do we want?
-
We are looking to update our "Brand" we already have a simple “home grown” logo and we are now looking for a new one, once we have this updated logo and businesses look and feel though the business card design we will refresh our website with the new logo and design thus updating the Companies overall look at feel.

Our current site is www.quorvix-example.net.au is a very basic wordpress site and we will be updating it once we have the new logo and designs done

Our initial thoughts on the new Quorvix identity are
• Logo Concept
- One of the key things is obviously the 8
- I was thinking that a logo that had 8 as the core of the logo would be cool,
- Almost like having a “ring” or hoop that is twisted to form an 8 with different services scribed on the inside.
- So we would have a Large 8 and the inside would have ring each service or section engraved.

• Brand / web Feel
- Simple
- Professional
- Innovative
- Clear
- Destination
- Unique
- Impartial
- Safe
- Leading edge
- Familiar

- Emerging technologies
- White and ice / glacier blue
- The familiar feel of the Brindle web site
- Embedded specialist Video clips

• Portfolio of Services
- Quorvix – A smart place for Smart people
- Quorvix – we provide the process to take ideas from awareness to reality
- Focus should be on the brand quality consistent clear local knowledge with regional, national, theatre and global presence

Access to Specialists
- Emerging technologies
- Sustainability
- Collaboration
- Data centre
- Virtualisation

• Adjacent ideas under the one Brand
- Tembrosk – Enable Business Collaboration
- Plinsk – Infrastructure Virtualisation
- morvo - smart people and processes
- skandel - Emerging technologies
- brunhavel - business to technology integration
- tolpin - Smart Infrastructure
- yusk – Connected communities
- dwol - sustainability

Target Market(s)

Australia, New Zealand and Asia pacific organisations that are typically English speaking.
Markets
- IT & Technology partners
- Banking and Finance
- Health

Industry/Entity Type

Business

Requirements
Must have
• Logo
Business cards
Colour pallette
3D Logo
Nice to have
• Style guide
Designer who can also assist with new Wordpress design
Should not have
• we don't want cheap looking, overtly flashy or gimmicky logo.

```html
<!DOCTYPE html>
<html lang="en">
<head>
<meta charset="utf-8">
<title>Quorvix – Business Card and Colour Palette</title>
<link rel="stylesheet" href="https://fonts.googleapis.com/css2?family=Open+Sans:ital,wght@0,400;0,600;0,700;1,600;1,700&display=swap">
<style>
  :root {
    --stage: #d9dadb;
    --card-white: #f4f8fa;
    --mint: #cde8e4;
    --navy: #14112e;
    --ice: #cde9f4;
    --teal: #80d0dc;
    --steel: #5a5f63;
    --frame: #ffffff;
    --label: #222222;
    --font: "Open Sans", Arial, sans-serif;
  }
  * { box-sizing: border-box; margin: 0; padding: 0; }
  html, body { width: 1200px; height: 900px; overflow: hidden; }
  body {
    background: var(--stage);
    font-family: var(--font);
    position: relative;
  }

  /* Card back */
  .card-back {
    position: absolute; left: 70px; top: 50px;
    width: 560px; height: 320px;
    background: var(--ice);
    display: flex; align-items: center; justify-content: center;
    box-shadow: 0 6px 18px rgba(0,0,0,.18);
  }
  .card-back .wordmark { font-size: 92px; }

  /* Shared wordmark */
  .wordmark {
    font-family: var(--font);
    font-weight: 700;
    color: var(--steel);
    letter-spacing: 1px;
    line-height: 1;
  }

  /* Card front */
  .card-front {
    position: absolute; left: 40px; top: 400px;
    width: 720px; height: 420px;
    background: var(--card-white);
    box-shadow: 0 8px 22px rgba(0,0,0,.22);
    display: flex; flex-direction: column;
  }
  .card-front .identity {
    flex: 1;
    display: flex; flex-direction: column; align-items: center; justify-content: center;
    gap: 14px;
    padding-top: 10px;
  }
  .card-front .wordmark { font-size: 84px; }
  .holder-name {
    font-size: 50px; font-weight: 400; color: var(--navy); line-height: 1;
  }
  .contact-row { display: flex; height: 62px; }
  .contact-cell {
    display: flex; align-items: center; justify-content: center;
    font-size: 15px; font-weight: 700; font-style: italic; color: var(--navy);
  }
  .contact-cell.address { width: 36%; background: var(--mint); justify-content: flex-start; padding-left: 18px; }
  .contact-cell.email { width: 33%; background: var(--ice); }
  .contact-cell.phone { width: 31%; background: var(--teal); }
  .web-band {
    height: 96px; background: var(--navy);
    display: flex; align-items: center; padding-left: 230px;
    color: var(--card-white); font-size: 34px; font-weight: 600;
  }

  /* Standalone logo */
  .logo-lockup {
    position: absolute; left: 720px; top: 190px;
  }
  .logo-lockup .wordmark { font-size: 104px; }

  /* Colour palette */
  .palette { position: absolute; left: 810px; top: 470px; }
  .swatch {
    position: absolute;
    width: 180px; height: 215px;
    background: var(--frame);
    border-radius: 8px;
    box-shadow: 0 3px 10px rgba(0,0,0,.25);
    padding: 10px;
  }
  .swatch .chip { height: 160px; border: 1px solid rgba(0,0,0,.06); }
  .swatch .codes {
    margin-top: 8px; font-size: 7.5px; font-weight: 600; color: var(--label);
    display: grid; grid-template-columns: 1fr auto; row-gap: 4px;
  }
  .swatch:nth-child(1) { left: 0; top: 0; }
  .swatch:nth-child(2) { left: 44px; top: 40px; }
  .swatch:nth-child(3) { left: 88px; top: 80px; }
  .swatch:nth-child(4) { left: 132px; top: 120px; }
  .swatch:nth-child(5) { left: 176px; top: 160px; }
  .chip.white { background: var(--card-white); }
  .chip.mint { background: var(--mint); }
  .chip.navy { background: var(--navy); }
  .chip.ice { background: var(--ice); }
  .chip.teal { background: var(--teal); }
</style>
</head>
<body>

  <section class="card-back">
    <span class="wordmark">Quorvix</span>
  </section>

  <section class="card-front">
    <div class="identity">
      <span class="wordmark">Quorvix</span>
      <span class="holder-name">Your Name</span>
    </div>
    <div class="contact-row">
      <div class="contact-cell address">1234 Street Name, City, State, Zip</div>
      <div class="contact-cell email">you@quorvix-example.com.au</div>
      <div class="contact-cell phone">Phone Number</div>
    </div>
    <div class="web-band">quorvix-example.com.au</div>
  </section>

  <div class="logo-lockup">
    <span class="wordmark">Quorvix</span>
  </div>

  <section class="palette" aria-label="Colour palette">
    <div class="swatch">
      <div class="chip white"></div>
      <div class="codes"><span>HTML: #f3f8fa</span><span></span><span>RGB: 243, 248, 250</span><span></span></div>
    </div>
    <div class="swatch">
      <div class="chip mint"></div>
      <div class="codes"><span>HTML: #cde8e4</span><span></span><span>RGB: 205, 232, 228</span><span></span></div>
    </div>
    <div class="swatch">
      <div class="chip navy"></div>
      <div class="codes"><span>HTML: #14112e</span><span></span><span>RGB: 20, 17, 46</span><span></span></div>
    </div>
    <div class="swatch">
      <div class="chip ice"></div>
      <div class="codes"><span>HTML: #cde9f4</span><span></span><span>RGB: 205, 233, 244</span><span></span></div>
    </div>
    <div class="swatch">
      <div class="chip teal"></div>
      <div class="codes"><span>HTML: #5c9149</span><span>CMYK: 69, 23.5, 92, 7</span><span>RGB: 92, 145, 73</span><span>PMS: n/a</span></div>
    </div>
  </section>

</body>
</html>
```